Apartment Hotel
Zielgruppe
Apartment Hotel, verkauf von Hotelzimmer, bzw. Apartments. Für kurzreisende oder Langzeitaufenthalte, für Touristen , Geschäftsleuten, Firmen.
Wir stellen komplette 1 oder 2 Zimmerapartments mit Küche.
www.apartment-hotel-feldburg.de
Aufgabenstellung
modernes Logo , Briefpapier & Visitenkarten , Layout,
Platz für Name/Position: Hotelmanager

```html
<!DOCTYPE html>
<html lang="de">
<head>
<meta charset="utf-8">
<title>Feldburg Apartmenthotel – Visitenkarte</title>
<link rel="stylesheet" href="https://fonts.googleapis.com/css2?family=Source+Sans+3:wght@300;400;600&display=swap">
<style>
  :root {
    --hotel-blue: #6196aa;
    --hotel-green: #9cc466;
    --paper: #ffffff;
    --backdrop: #e8eee5;
  }
  html, body {
    margin: 0;
    padding: 0;
    overflow: hidden;
  }
  body {
    width: 1200px;
    height: 1200px;
    background: var(--backdrop);
    position: relative;
    font-family: "Source Sans 3", "Myriad Pro", Arial, sans-serif;
  }
  .card {
    position: absolute;
    box-sizing: border-box;
    width: 578px;
    height: 374px;
  }
  .card-front {
    left: 98px;
    top: 233px;
    background: var(--hotel-blue);
    border: 10px solid var(--paper);
  }
  .card-back {
    left: 530px;
    top: 483px;
    width: 576px;
    height: 374px;
    background: var(--paper);
    border: 9px solid var(--hotel-green);
    text-align: center;
  }
  .brand {
    display: flex;
    align-items: center;
    justify-content: center;
    gap: 14px;
    color: var(--hotel-green);
    font-weight: 600;
    letter-spacing: 0.04em;
    line-height: 1;
  }
  .brand-mark {
    width: 20px;
    height: 20px;
  }
  .card-front .brand {
    font-size: 52px;
    margin-top: 210px;
  }
  .card-front .brand-mark { background: var(--paper); }
  .card-back .brand {
    font-size: 40px;
    margin-top: 128px;
  }
  .card-back .brand-mark {
    background: var(--hotel-blue);
    width: 16px;
    height: 16px;
  }
  .person-name {
    margin: 50px 0 0;
    font-size: 20px;
    line-height: 24px;
    font-weight: 600;
    color: var(--hotel-green);
  }
  .person-role {
    margin: 4px 0 0;
    font-size: 13px;
    line-height: 18px;
    letter-spacing: 0.06em;
    text-transform: uppercase;
    color: var(--hotel-blue);
  }
  .contact {
    margin: 18px 0 0;
    font-size: 15px;
    font-weight: 300;
    line-height: 25px;
    color: var(--hotel-blue);
  }
  .contact p { margin: 0; }
  .contact .web {
    font-weight: 600;
    color: var(--hotel-green);
    margin-top: 2px;
  }
</style>
</head>
<body>
  <section class="card card-front" aria-label="Vorderseite">
    <div class="brand"><span class="brand-mark"></span><span>Feldburg</span></div>
  </section>

  <section class="card card-back" aria-label="Rückseite">
    <div class="brand"><span class="brand-mark"></span><span>Feldburg</span></div>
    <p class="person-name">Anja Kessler</p>
    <p class="person-role">Hotelmanager</p>
    <div class="contact">
      <p>Apartment Hotel Feldburg • Gartenstrasse 12 • 99089 Erfurt</p>
      <p>T +49 361 48 27 6-03 • F +49 361 48 27 6-88 • M info@hotel-feldburg.de</p>
      <p class="web">www.apartment-hotel-feldburg.de</p>
    </div>
  </section>
</body>
</html>
```